Consulting firm needs an infographic

The consulting we do needs a very graphic and understandable way to have perspective clients get exactly where we can help their company grow. I designed something that needs a lot of spice for it to look professional and relatable to them. This is being created to be used on a business card, as well as on posters, and social media.

```html
<!DOCTYPE html>
<html lang="en">
<head>
<meta charset="utf-8">
<title>Consulting Growth Infographic</title>
<link href="https://fonts.googleapis.com/css2?family=Montserrat:wght@400;500;700;800&display=swap" rel="stylesheet">
<style>
  :root {
    --paper: #ffffff;
    --map-tone: #e4e5e6;
    --map-tone-soft: #eeeff0;
    --track: #cfd0d2;
    --green: #3bb44a;
    --green-light: #a8cf38;
    --green-dark: #5aa83f;
    --orange: #f15a2b;
    --orange-light: #fbb040;
    --orange-mid: #f7941d;
    --blue: #1a9ad6;
    --blue-dark: #0b6fb8;
    --ink: #231f20;
    --ink-soft: #3a3a3a;
    --white: #ffffff;
  }
  html, body {
    margin: 0;
    padding: 0;
    width: 1200px;
    height: 848px;
    overflow: hidden;
    background: var(--paper);
  }
  .canvas {
    position: relative;
    width: 1200px;
    height: 848px;
    font-family: "Montserrat", sans-serif;
  }
  .world-map {
    position: absolute;
    left: 10px;
    top: 160px;
    width: 1180px;
    height: 640px;
    border-radius: 40px;
    background: radial-gradient(ellipse at 50% 45%, var(--map-tone-soft), var(--map-tone) 70%, var(--paper) 100%);
    opacity: 0.8;
  }
  .brand-card {
    position: absolute;
    left: 998px;
    top: 70px;
    width: 120px;
    height: 78px;
    background: var(--white);
    border-radius: 12px;
    box-shadow: 0 3px 6px rgba(0,0,0,0.25);
    display: flex;
    align-items: center;
    justify-content: center;
    gap: 7px;
  }
  .brand-card .brand-dot {
    width: 12px;
    height: 12px;
    border-radius: 50%;
    background: var(--orange);
  }
  .brand-card .brand-name {
    font-weight: 800;
    font-size: 15px;
    color: var(--ink);
    line-height: 1.05;
  }
  .diagram {
    position: absolute;
    left: 0;
    top: 0;
  }
  .node-label {
    font-family: "Montserrat", sans-serif;
    font-size: 12.5px;
    font-weight: 400;
    fill: var(--white);
  }
  .step-number {
    font-family: "Montserrat", sans-serif;
    font-size: 40px;
    font-weight: 800;
    fill: var(--white);
  }
  .company-title {
    font-family: "Montserrat", sans-serif;
    font-size: 27px;
    font-weight: 800;
    fill: var(--ink);
  }
  .company-sub {
    font-family: "Montserrat", sans-serif;
    font-size: 11px;
    font-weight: 700;
    fill: var(--ink-soft);
  }
</style>
</head>
<body>
<div class="canvas">
  <div class="world-map" role="img" aria-label="Light grey world map spread behind the diagram"></div>

  <div class="brand-card">
    <span class="brand-dot"></span>
    <span class="brand-name">Fieldmark<br>Advisory</span>
  </div>

  <svg class="diagram" width="1200" height="848" viewBox="0 0 1200 848">
    <defs>
      <linearGradient id="green-fan" x1="0" y1="1" x2="1" y2="0">
        <stop offset="0" stop-color="var(--green-light)"/>
        <stop offset="1" stop-color="var(--green-dark)"/>
      </linearGradient>
      <linearGradient id="orange-fan" x1="0" y1="0" x2="0" y2="1">
        <stop offset="0" stop-color="var(--orange-light)"/>
        <stop offset="1" stop-color="var(--orange)"/>
      </linearGradient>
      <linearGradient id="blue-fan" x1="0" y1="0" x2="1" y2="1">
        <stop offset="0" stop-color="var(--blue)"/>
        <stop offset="1" stop-color="var(--blue-dark)"/>
      </linearGradient>
      <linearGradient id="blue-node" x1="0" y1="1" x2="1" y2="0">
        <stop offset="0" stop-color="var(--blue-dark)"/>
        <stop offset="1" stop-color="var(--blue)"/>
      </linearGradient>
      <radialGradient id="company-face" cx="0.45" cy="0.4" r="0.7">
        <stop offset="0" stop-color="#ffffff"/>
        <stop offset="1" stop-color="#e6e6e7"/>
      </radialGradient>
      <filter id="soft-shadow" x="-30%" y="-30%" width="160%" height="160%">
        <feDropShadow dx="0" dy="4" stdDeviation="6" flood-color="#000" flood-opacity="0.25"/>
      </filter>
    </defs>

    <!-- outer track -->
    <g class="track">
      <path d="M256 574 A330 330 0 0 1 916 574" fill="none" stroke="var(--track)" stroke-width="20"/>
      <path d="M266 574 A320 320 0 0 1 906 574" fill="none" stroke="var(--white)" stroke-width="1.5" stroke-dasharray="5 4"/>
    </g>

    <!-- fan segments -->
    <g class="fan">
      <path d="M586 574 L298 574 A288 288 0 0 1 425 335 Z" fill="url(#green-fan)"/>
      <path d="M586 574 L456 340 A268 268 0 0 1 716 340 Z" fill="url(#orange-fan)"/>
      <path d="M586 574 L747 335 A288 288 0 0 1 874 574 Z" fill="url(#blue-fan)"/>
    </g>

    <!-- step numbers -->
    <text class="step-number" x="322" y="558">01</text>
    <text class="step-number" x="472" y="372">02</text>
    <text class="step-number" x="716" y="410">03</text>

    <!-- flow chevrons -->
    <g class="chevrons">
      <g fill="var(--green)" transform="translate(388 276) rotate(-35)">
        <path d="M-22 -10 L-8 -10 L2 0 L-8 10 L-22 10 L-12 0 Z"/>
        <path d="M-2 -10 L12 -10 L22 0 L12 10 L-2 10 L8 0 Z"/>
      </g>
      <g fill="var(--orange)" transform="translate(762 268) rotate(30)">
        <path d="M-22 -10 L-8 -10 L2 0 L-8 10 L-22 10 L-12 0 Z"/>
        <path d="M-2 -10 L12 -10 L22 0 L12 10 L-2 10 L8 0 Z"/>
      </g>
      <g fill="var(--white)" transform="translate(586 408)">
        <path d="M-26 -13 L-10 -13 L2 0 L-10 13 L-26 13 L-14 0 Z"/>
        <path d="M-2 -13 L14 -13 L26 0 L14 13 L-2 13 L10 0 Z"/>
      </g>
      <g fill="var(--white)" transform="translate(446 502) rotate(215)">
        <path d="M-24 -12 L-10 -12 L2 0 L-10 12 L-24 12 L-12 0 Z"/>
        <path d="M-2 -12 L12 -12 L24 0 L12 12 L-2 12 L10 0 Z"/>
      </g>
      <g fill="var(--white)" transform="translate(730 496) rotate(150)">
        <path d="M-24 -12 L-10 -12 L2 0 L-10 12 L-24 12 L-12 0 Z"/>
        <path d="M-2 -12 L12 -12 L24 0 L12 12 L-2 12 L10 0 Z"/>
      </g>
    </g>

    <!-- node: vendors -->
    <g class="node node-vendors">
      <circle cx="313" cy="432" r="81" fill="var(--white)" filter="url(#soft-shadow)"/>
      <circle cx="313" cy="432" r="70" fill="var(--green)"/>
      <g class="icon-money-bag" fill="var(--white)">
        <path d="M307 380 L319 380 L315 390 L311 390 Z"/>
        <path d="M310 391 L316 391 C332 398 338 412 334 420 C331 426 324 428 313 428 C302 428 295 426 292 420 C288 412 294 398 310 391 Z"/>
      </g>
      <text x="313" y="421" text-anchor="middle" font-family="Montserrat, sans-serif" font-weight="800" font-size="16" fill="var(--green)">$</text>
      <text class="node-label" text-anchor="middle">
        <tspan x="313" y="449">Vendors</tspan>
        <tspan x="313" y="464">Resources</tspan>
        <tspan x="313" y="479">Costs</tspan>
      </text>
    </g>

    <!-- node: executives -->
    <g class="node node-executives">
      <circle cx="580" cy="274" r="81" fill="var(--white)" filter="url(#soft-shadow)"/>
      <circle cx="580" cy="274" r="70" fill="var(--orange)"/>
      <g class="icon-search" fill="none" stroke="var(--white)">
        <circle cx="575" cy="237" r="12" stroke-width="3"/>
        <path d="M584 246 L597 259" stroke-width="5" stroke-linecap="round"/>
      </g>
      <text class="node-label" text-anchor="middle">
        <tspan x="580" y="284">Executives</tspan>
        <tspan x="580" y="298">Administratives</tspan>
        <tspan x="580" y="312">Personnels</tspan>
        <tspan x="580" y="327">Logistics</tspan>
      </text>
    </g>

    <!-- node: customers -->
    <g class="node node-customers">
      <circle cx="852" cy="432" r="81" fill="var(--white)" filter="url(#soft-shadow)"/>
      <circle cx="852" cy="432" r="70" fill="url(#blue-node)"/>
      <g class="icon-person" fill="var(--white)">
        <circle cx="852" cy="394" r="12"/>
        <path d="M831 425 C831 412 840 407 852 407 C864 407 873 412 873 425 Z"/>
      </g>
      <text class="node-label" text-anchor="middle">
        <tspan x="852" y="451">Customers</tspan>
        <tspan x="852" y="466">Identify &amp; B&amp;M</tspan>
        <tspan x="852" y="480">Revenue</tspan>
      </text>
    </g>

    <!-- centre: company -->
    <g class="company-hub">
      <circle cx="589" cy="578" r="121" fill="#d9dadb" filter="url(#soft-shadow)"/>
      <circle cx="589" cy="578" r="104" fill="url(#company-face)"/>
      <text class="company-title" text-anchor="middle">
        <tspan x="589" y="535">YOUR</tspan>
        <tspan x="589" y="565">COMPANY</tspan>
      </text>
      <text class="company-sub" x="589" y="586" text-anchor="middle">PRODUCTS/SERVICES</text>
      <path d="M532 605 Q589 603 646 605" stroke="var(--ink-soft)" stroke-width="1.5" fill="none"/>
      <text class="company-sub" text-anchor="middle">
        <tspan x="589" y="631">Workforce | Workplace</tspan>
        <tspan x="589" y="646">Workflow</tspan>
      </text>
    </g>
  </svg>
</div>
</body>
</html>
```